Brightwell Systems, a software development company, needs a website

We need a website to promote our software development company. The company is brand new and we want to market ourselves. We develop all kinds of software from web applications, to desktop applications, to mobile applications. Small company, not a lot of history, just need something flashy.

```html
<!DOCTYPE html>
<html lang="en">
<head>
<meta charset="utf-8">
<title>Brightwell Systems — Software Development</title>
<link href="https://fonts.googleapis.com/css2?family=Mulish:wght@300;400;600;700&family=Montserrat:wght@400;600;700;800&family=Share+Tech+Mono&display=swap" rel="stylesheet">
<style>
:root{
  --panel:#262626;
  --ink:#2b2b2b;
  --text:#555;
  --muted:#9a9a9a;
  --accent:#17aad0;
  --line:#d4d4d4;
  --light:#e4e4e4;
  --white:#fff;
  --num:#4a4a4a;
}
*{margin:0;padding:0;box-sizing:border-box}
html,body{width:1200px;height:4886px;overflow:hidden;background:var(--white)}
body{position:relative;font-family:"Mulish",sans-serif;color:var(--text)}
.abs{position:absolute}
a{color:inherit;text-decoration:none}

/* header */
.brand{position:absolute;left:123px;top:26px;text-align:center;width:220px}
.brand-name{font-family:"Mulish",sans-serif;font-weight:700;font-size:36px;color:var(--accent);letter-spacing:1px;line-height:1}
.brand-sub{font-size:11px;letter-spacing:9px;color:var(--ink);margin-top:8px}
.nav{position:absolute;top:52px;left:0;width:1200px;font-size:11px;font-weight:600;color:var(--ink);text-transform:uppercase}
.nav span{position:absolute}
.nav .active{color:var(--accent)}
.nav .active::before{content:"";position:absolute;left:-14px;top:-10px;width:30px;height:2px;background:var(--accent)}
.nav .active::after{content:"";position:absolute;left:6px;bottom:-10px;width:58px;height:2px;background:var(--accent)}

/* hero */
.hero-kicker{left:123px;top:216px;font-size:22px;letter-spacing:3px;color:var(--ink);font-weight:400}
.hero-tag{left:121px;top:244px;font-family:"Montserrat",sans-serif;font-size:56px;font-weight:400;color:var(--ink);letter-spacing:1px}
.hero-tag b{color:var(--accent);font-weight:400}
.hero-title{left:121px;top:318px;font-family:"Montserrat",sans-serif;font-size:68px;font-weight:800;line-height:76px;color:var(--ink);letter-spacing:1px}
.hero-frame{left:398px;top:173px;width:214px;height:331px;border:13px solid var(--accent);border-right:none}
.photo{background:linear-gradient(135deg,#8a8a8a,#4d4d4d 55%,#b5a79a)}
.social{display:flex;gap:11px}
.social i{display:block;width:24px;height:24px;border-radius:50%;border:1.5px solid var(--ink)}
.social i.on{background:var(--accent);border-color:var(--accent)}

/* shared panels */
.panel{position:absolute;background:var(--panel)}
.num{position:absolute;font-family:"Share Tech Mono",monospace;font-size:58px;color:var(--num);letter-spacing:4px;line-height:1}
.vert{position:absolute;writing-mode:vertical-rl;transform:rotate(180deg);font-size:14px;letter-spacing:11px;color:#5a5a5a;text-transform:uppercase}
.view-all{position:absolute;font-size:15px;letter-spacing:2px;color:#e8e8e8;width:120px;text-align:center}
.view-all::before{content:"";position:absolute;left:20px;top:-6px;width:38px;height:1px;background:#bbb}
.view-all::after{content:"";position:absolute;right:20px;bottom:-6px;width:38px;height:1px;background:#bbb}

/* about */
.about-title{left:696px;top:766px;font-size:31px;color:var(--ink);font-weight:400}
.about-copy{left:696px;top:822px;width:378px;font-size:12.5px;line-height:19px;color:#777}
.about-copy p{margin-bottom:11px}
.more{left:706px;top:1076px;font-size:14px;color:var(--accent)}
.more::after{content:"";position:absolute;left:-4px;bottom:-7px;width:92px;height:1px;background:var(--accent)}

/* services */
.svc-card{position:absolute;left:123px;top:1361px;width:313px;height:216px;background:var(--white);box-shadow:0 2px 14px rgba(0,0,0,.09)}
.svc{position:absolute;width:300px;text-align:center}
.svc svg{display:block;margin:0 auto 10px}
.svc h3{font-size:13px;font-weight:600;letter-spacing:.5px;color:var(--ink);margin-bottom:12px}
.svc h3.hl{color:var(--accent)}
.svc p{font-size:12.5px;line-height:20px;color:#888;padding:0 6px}

/* work */
.filters{left:298px;top:1926px;font-size:12px;color:#e0e0e0}
.filters li{list-style:none;height:41px}
.filters li.on{color:var(--accent)}
.tile{position:absolute}
.wd-card{position:absolute;left:436px;top:2070px;width:411px;height:171px;background:#f7f7f7;box-shadow:0 2px 10px rgba(0,0,0,.12);text-align:center}
.wd-card span{display:block;margin-top:60px;font-size:10px;letter-spacing:2px;color:#333;font-weight:600}
.wd-card i{display:block;width:30px;height:30px;border-radius:50%;border:1px solid #bbb;margin:10px auto 0}

/* team */
.lead-name{left:127px;top:2578px;font-size:21px;color:var(--ink);letter-spacing:.5px}
.lead-role{left:127px;top:2614px;font-size:8px;letter-spacing:2px;color:#aaa}
.lead-sep{left:320px;top:2590px;width:1px;height:56px;background:var(--line)}
.lead-quote{left:356px;top:2596px;width:240px;font-size:12.5px;line-height:20px;color:#888}
.member-name{font-size:17px;color:var(--ink)}
.member-role{font-size:8px;letter-spacing:2px;color:#aaa}

/* testimonials */
.quote-card{position:absolute;left:368px;top:3204px;width:707px;height:385px;background:var(--white);box-shadow:0 3px 18px rgba(0,0,0,.1);text-align:center}
.quote-mark{font-family:"Montserrat",sans-serif;font-size:90px;line-height:1;color:#ddd;font-weight:800;margin-top:28px;height:60px}
.quote-text{font-size:12.5px;line-height:26px;color:#888;margin-top:14px}
.quote-name{font-size:18px;color:var(--ink);margin-top:18px}
.quote-role{font-size:8px;letter-spacing:2px;color:#aaa;margin-top:6px}
.avatars{display:flex;justify-content:center;align-items:center;gap:34px;margin-top:28px}
.avatars i{display:block;border-radius:50%;background:linear-gradient(135deg,#bbb,#555);box-shadow:0 2px 8px rgba(0,0,0,.2)}

/* blog */
.post-title{font-size:17px;color:var(--ink);letter-spacing:.3px}
.post-text{font-size:11.5px;line-height:20px;color:#888;width:254px}
.post-more{font-size:9px;letter-spacing:2px;color:#444}
.post-date{position:absolute;writing-mode:vertical-rl;transform:rotate(180deg);font-size:9px;letter-spacing:2px;color:#bbb}

/* footer */
.foot-left{position:absolute;left:0;top:4317px;width:599px;height:514px;background:var(--light)}
.foot-right{position:absolute;left:599px;top:4317px;width:601px;height:514px;background:var(--panel)}
.foot-h{font-size:21px;color:var(--ink)}
.foot-p{font-size:11.5px;line-height:21px;color:#666;width:270px}
.foot-info{font-size:11.5px;line-height:20px;color:#555}
.foot-info b{color:var(--ink)}
.field{position:absolute;left:696px;width:379px;font-size:11px;color:#bbb;border-bottom:1px solid #666;padding-bottom:14px}
.send{position:absolute;left:836px;top:4758px;width:95px;text-align:center;font-size:15px;color:#e8e8e8;letter-spacing:1px}
.send::before{content:"";position:absolute;left:0;top:-6px;width:40px;height:1px;background:#bbb}
.send::after{content:"";position:absolute;right:0;bottom:-6px;width:40px;height:1px;background:#bbb}
.copyright{left:127px;top:4850px;font-size:11px;color:#666}
</style>
</head>
<body>

<!-- header -->
<div class="brand"><div class="brand-name">BRIGHTWELL</div><div class="brand-sub">SYSTEMS</div></div>
<nav class="nav">
  <span class="active" style="left:597px">Home</span>
  <span style="left:664px">About ▾</span>
  <span style="left:745px">Our Blog</span>
  <span style="left:832px">Mobile ▾</span>
  <span style="left:920px">Contact Us</span>
  <span style="left:1024px;top:-3px">
    <svg width="14" height="14" viewBox="0 0 14 14"><circle cx="6" cy="6" r="4.2" fill="none" stroke="#2b2b2b" stroke-width="1.8"/><line x1="9" y1="9" x2="13" y2="13" stroke="#2b2b2b" stroke-width="2"/></svg>
  </span>
  <span style="left:1060px;top:-3px">
    <svg width="15" height="13" viewBox="0 0 15 13"><path d="M1 5 L7.5 1 L14 5 V12 H1 Z" fill="#2b2b2b"/><path d="M1 5 L7.5 9 L14 5" fill="none" stroke="#fff" stroke-width="1"/></svg>
  </span>
</nav>

<!-- hero -->
<div class="abs hero-kicker">WE LOVE TO</div>
<div class="hero-frame abs"></div>
<div class="abs hero-tag"><b>#</b>BRIGHTWELL</div>
<div class="abs hero-title">CREATIVE<br>PASSION</div>
<div class="abs photo" role="img" aria-label="Team gathered around a desk reviewing work in a bright office" style="left:612px;top:125px;width:463px;height:429px"></div>
<div class="abs social" style="left:126px;top:526px"><i class="on"></i><i></i><i></i><i></i></div>

<!-- 01 about -->
<div class="panel" style="left:123px;top:637px;width:302px;height:601px"></div>
<div class="num" style="left:157px;top:690px">01</div>
<div class="vert" style="left:258px;top:690px">About Us</div>
<div class="abs photo" role="img" aria-label="Developer working at a desktop computer, black and white" style="left:341px;top:702px;width:302px;height:470px;background:linear-gradient(160deg,#6a6a6a,#2f2f2f 50%,#9a9a9a)"></div>
<h2 class="abs about-title">About Us</h2>
<div class="abs about-copy">
  <p>Sed ut perspiciatis unde omnis iste natus error sit voluptatem accusantium dolorem laudantium, totam rem aperiam, eaque ipsa quae ab illo inventore veritatis et quasi architecto beatae vitae dicta sunt explicabo.</p>
  <p>Nemo enim ipsam voluptatem quia voluptas sit aspernatur aut odit aut fugit, sed ttquia consequuntur magni dolores eos qui ratione voluptatem sequi nesciunt.</p>
  <p>Neque porro quisquam est, qui dolorem ipsum quia dolor sit amet, consectetur, adipisci velit, sed quia non numquam eius modi tempora incidunt ut labore et dolore magnam aliquam quaerat voluptatem.</p>
</div>
<a class="abs more">Read More</a>

<!-- 02 services -->
<div class="panel" style="left:775px;top:1321px;width:300px;height:514px"></div>
<div class="num" style="left:955px;top:1368px">02</div>
<div class="vert" style="left:884px;top:1362px">Our Services</div>
<div class="view-all" style="left:867px;top:1767px">View All</div>

<div class="svc-card"></div>
<div class="svc" style="left:130px;top:1390px">
  <svg width="40" height="36" viewBox="0 0 40 36"><rect x="3" y="3" width="30" height="24" fill="none" stroke="#17aad0" stroke-width="2"/><line x1="3" y1="9" x2="33" y2="9" stroke="#17aad0" stroke-width="2"/><line x1="9" y1="15" x2="21" y2="15" stroke="#17aad0" stroke-width="2"/><line x1="9" y1="20" x2="17" y2="20" stroke="#17aad0" stroke-width="2"/><circle cx="31" cy="27" r="6" fill="#fff" stroke="#17aad0" stroke-width="2"/></svg>
  <h3 class="hl">SOFTWARE DEVELOPMENT</h3>
  <p>Lorem ipsum dolor sit amet, consectetur adipiscing elit, sed do eiusmod tempor incididunt ut labore et dolore magna aliqua.</p>
</div>
<div class="svc" style="left:440px;top:1390px">
  <svg width="40" height="36" viewBox="0 0 40 36"><path d="M6 18 L24 8 V30 L6 22 Z" fill="none" stroke="#17aad0" stroke-width="2"/><rect x="2" y="17" width="5" height="6" fill="none" stroke="#17aad0" stroke-width="2"/><line x1="28" y1="14" x2="34" y2="10" stroke="#17aad0" stroke-width="2"/><line x1="29" y1="19" x2="36" y2="19" stroke="#17aad0" stroke-width="2"/></svg>
  <h3>BRANDING</h3>
  <p>Lorem ipsum dolor sit amet, consectetur adipiscing elit, sed do eiusmod tempor incididunt ut labore et dolore magna aliqua.</p>
</div>
<div class="svc" style="left:130px;top:1604px">
  <svg width="40" height="36" viewBox="0 0 40 36"><rect x="3" y="3" width="34" height="22" fill="none" stroke="#17aad0" stroke-width="2"/><path d="M15 10 L11 14 L15 18 M25 10 L29 14 L25 18 M22 9 L18 19" fill="none" stroke="#17aad0" stroke-width="2"/><line x1="14" y1="31" x2="26" y2="31" stroke="#17aad0" stroke-width="2"/></svg>
  <h3>WEBSITE DEVELOPMENT</h3>
  <p>Lorem ipsum dolor sit amet, consectetur adipiscing elit, sed do eiusmod tempor incididunt ut labore et dolore magna aliqua.</p>
</div>
<div class="svc" style="left:440px;top:1604px">
  <svg width="40" height="36" viewBox="0 0 40 36"><rect x="3" y="3" width="34" height="24" fill="none" stroke="#17aad0" stroke-width="2"/><line x1="9" y1="10" x2="31" y2="10" stroke="#17aad0" stroke-width="2"/><line x1="9" y1="15" x2="24" y2="15" stroke="#17aad0" stroke-width="2"/><line x1="9" y1="20" x2="28" y2="20" stroke="#17aad0" stroke-width="2"/><line x1="14" y1="32" x2="26" y2="32" stroke="#17aad0" stroke-width="2"/></svg>
  <h3>WEBSITE DESIGNING</h3>
  <p>Lorem ipsum dolor sit amet, consectetur adipiscing elit, sed do eiusmod tempor incididunt ut labore et dolore magna aliqua.</p>
</div>

<!-- 03 work -->
<div class="panel" style="left:123px;top:1877px;width:302px;height:557px"></div>
<div class="num" style="left:150px;top:1926px">03</div>
<div class="vert" style="left:251px;top:1930px">Our Work</div>
<ul class="abs filters">
  <li class="on">All</li><li>Mobile App</li><li>Branding</li><li>Web Design</li><li>Development</li><li>Illustrator</li>
</ul>
<div class="view-all" style="left:215px;top:2360px">View All</div>

<div class="tile" role="img" aria-label="Paper crane on white surface" style="left:425px;top:1877px;width:216px;height:186px;background:linear-gradient(135deg,#f2f2f2,#d6d6d6)"></div>
<div class="tile" role="img" aria-label="Framed landscape print" style="left:641px;top:1877px;width:216px;height:186px;background:linear-gradient(135deg,#555,#cfcfcf 55%,#efefef)"></div>
<div class="tile" role="img" aria-label="Coffee cup, notebook and glasses on marble" style="left:857px;top:1877px;width:218px;height:372px;background:linear-gradient(160deg,#ececec,#d4d4d4)"></div>
<div class="tile" role="img" aria-label="Light grey studio backdrop" style="left:425px;top:2063px;width:432px;height:186px;background:#ededed"></div>
<div class="wd-card"><span>WEB DESIGN</span><i></i></div>
<div class="tile" role="img" aria-label="Framed architectural print" style="left:425px;top:2249px;width:216px;height:185px;background:linear-gradient(135deg,#f0f0f0,#bdbdbd)"></div>
<div class="tile" role="img" aria-label="Tablet and phone on marble desk" style="left:641px;top:2249px;width:434px;height:185px;background:linear-gradient(160deg,#e6e6e6,#9a9a9a 60%,#2a2a2a)"></div>

<!-- 04 team -->
<div class="panel" style="left:775px;top:2520px;width:300px;height:514px"></div>
<div class="num" style="left:955px;top:2566px">04</div>
<div class="vert" style="left:910px;top:2560px">Our Team</div>
<div class="view-all" style="left:867px;top:2962px">View All</div>
<div class="abs" role="img" aria-label="Portrait of a bearded team member in sunglasses" style="left:614px;top:2560px;width:243px;height:436px;background:linear-gradient(180deg,#ffffff,#cfcfcf 40%,#777)"></div>

<div class="abs lead-name">Darian Holt</div>
<div class="abs lead-role">CREATIVE DIRECTOR</div>
<div class="abs social" style="left:127px;top:2648px"><i class="on"></i><i></i><i></i><i></i></div>
<div class="abs lead-sep"></div>
<div class="abs lead-quote">Lorem ipsum dolor sit amet, consectetur adipiscing elit, sed do eiusmod tempor aliqua.</div>

<div class="abs" role="img" aria-label="Portrait of Sophia Marlow" style="left:125px;top:2721px;width:218px;height:275px;background:linear-gradient(180deg,#e8e8e8,#9a9a9a 60%,#333)"></div>
<div class="abs" role="img" aria-label="Portrait of Emily Corwin" style="left:366px;top:2721px;width:218px;height:275px;background:linear-gradient(180deg,#e8e8e8,#a8a8a8 60%,#555)"></div>
<div class="abs" style="left:136px;top:3005px"><div class="member-name">Sophia Marlow</div><div class="member-role">CREATIVE DIRECTOR</div></div>
<div class="abs" style="left:380px;top:3005px"><div class="member-name">Emily Corwin</div><div class="member-role">CREATIVE DIRECTOR</div></div>

<!-- 05 testimonials -->
<div class="panel" style="left:123px;top:3119px;width:302px;height:559px"></div>
<div class="num" style="left:150px;top:3170px">05</div>
<div class="vert" style="left:251px;top:3170px">Testimonials</div>
<div class="view-all" style="left:215px;top:3604px">View All</div>
<div class="quote-card">
  <div class="quote-mark">“</div>
  <div class="quote-text">“I am so happy because I found this Clearview, and it just<br>made my life easier.Thanks so much for sharing”</div>
  <div class="quote-name">Julian Reyes</div>
  <div class="quote-role">CREATIVE DIRECTOR</div>
  <div class="avatars">
    <i role="img" aria-label="Client portrait" style="width:58px;height:58px"></i>
    <i role="img" aria-label="Julian Reyes portrait" style="width:84px;height:84px"></i>
    <i role="img" aria-label="Client portrait" style="width:58px;height:58px"></i>
  </div>
</div>

<!-- 06 blog -->
<div class="panel" style="left:775px;top:3720px;width:300px;height:510px"></div>
<div class="num" style="left:955px;top:3766px">06</div>
<div class="vert" style="left:910px;top:3762px">Our Blog</div>
<div class="view-all" style="left:867px;top:4158px">View All</div>

<div class="abs" role="img" aria-label="Team meeting around a table, black and white" style="left:125px;top:3769px;width:218px;height:142px;background:linear-gradient(135deg,#d8d8d8,#555)"></div>
<div class="post-date" style="left:407px;top:3762px">By Holt, 1 week ago</div>
<div class="abs post-title" style="left:474px;top:3755px">We Do The Best Design</div>
<div class="abs post-text" style="left:474px;top:3789px">Lorem ipsum dolor sit amet, consectetur adipiscing elit, sed do eiusmod tempor incididunt ut labore et dolore magna aliqua. Ut enim mco laboris nisi ut aliquip consequat.</div>
<div class="abs post-more" style="left:474px;top:3897px">CONTINUE &nbsp;→</div>

<div class="abs post-title" style="left:120px;top:4008px;width:248px;text-align:right">We Do The Best Design</div>
<div class="abs post-text" style="left:114px;top:4042px;text-align:right">Lorem ipsum dolor sit amet, consectetur aing elit, sed do eiusmod tempor incididuntlabore et dolore magna aliqua. Ut enim mco laboris nisi ut aliquip consequat.</div>
<div class="abs post-more" style="left:287px;top:4149px">CONTINUE &nbsp;→</div>
<div class="post-date" style="left:407px;top:4010px">By Holt, 1 week ago</div>
<div class="abs" role="img" aria-label="Open-plan office with people at desks, black and white" style="left:476px;top:4014px;width:220px;height:146px;background:linear-gradient(135deg,#cfcfcf,#4a4a4a)"></div>

<!-- footer -->
<div class="foot-left"></div>
<div class="foot-right"></div>
<div class="abs foot-h" style="left:123px;top:4401px">Contact Us</div>
<div class="abs foot-p" style="left:123px;top:4448px">Lorem ipsum dolor sit amet, consectetur aing elit, sed do eiusmod tempor incididuntlabore et dolore magna aliqua.</div>
<div class="abs foot-info" style="left:123px;top:4540px">
  <b>Address:</b><br>No. 48, Harbor Lane,<br>Westfield City<br>
  <div style="margin-top:8px"><b>Phone:</b> 210.4470.0000</div>
  <div style="margin-top:8px"><b>E-mail:</b> hello@brightwell.example</div>
</div>
<div class="abs" style="left:123px;top:4752px;text-align:center">
  <div style="font-weight:700;font-size:19px;color:var(--accent);line-height:1">BRIGHTWELL</div>
  <div style="font-size:6px;letter-spacing:5px;color:var(--ink);margin-top:4px">SYSTEMS</div>
</div>

<div class="abs foot-h" style="left:667px;top:4401px;color:#eee">Get In Touch</div>
<div class="field" style="top:4452px">Name</div>
<div class="field" style="top:4512px">Email</div>
<div class="field" style="top:4572px">Phone</div>
<div class="field" style="top:4632px;padding-bottom:55px">Massage</div>
<div class="send">Send</div>

<div class="abs copyright">© 2019 Brightwell Systems. All Right Reserved</div>
<div class="abs social" style="left:937px;top:4845px"><i class="on"></i><i></i><i></i><i></i></div>

</body>
</html>
```